Business Card Design

Harbor Refuse 342 is a waste collection business contracted to remove waste from city streets, parks and caravan parks.

Target Market(s)

CEO and Managing Directors

Industry/Entity Type

Business

Contact Information for Business Card

Harbor Refuse 342
Manager
Dale Pickett
0439516204
harborrefuse342@quillmail.com.au

Colors
33a6d7
ecf7fb

Requirements
Must have
• Must have eye catching design that stands out above others ( tender process can be very competitive ).
Nice to have
• A garbage truck on or in the logo somehow

```html
<!DOCTYPE html>
<html lang="en">
<head>
<meta charset="utf-8">
<title>Harbor Refuse 342 – Business Card</title>
<link rel="stylesheet" href="https://fonts.googleapis.com/css2?family=Roboto:wght@500;700&display=swap">
<style>
  :root {
    --brand-blue: #33a6d7;
    --brand-blue-deep: #1a8fc4;
    --brand-ice: #ecf7fb;
    --sheet-top: #dde2e6;
    --sheet-white: #ffffff;
    --rule-silver: #9aa0a5;
    --panel-black: #0b0c0d;
    --panel-charcoal: #1b1d1f;
    --text-grey: #c9ccce;
    --text-white: #f4f5f6;
    --page-bg: #ffffff;
  }
  * { margin: 0; padding: 0; box-sizing: border-box; }
  html, body {
    width: 1200px;
    height: 900px;
    overflow: hidden;
    background: var(--page-bg);
    font-family: "Roboto", Arial, sans-serif;
  }
  .business-card {
    position: absolute;
    left: 150px;
    top: 190px;
    width: 900px;
    height: 520px;
    border-radius: 40px;
    overflow: hidden;
    background: var(--panel-black);
    box-shadow: 0 0 0 1px #e3e6e8;
  }
  .card-header {
    position: absolute;
    left: 0; top: 0;
    width: 100%;
    height: 262px;
    background: linear-gradient(180deg, var(--sheet-top) 0%, var(--sheet-white) 70%);
  }
  .truck-artwork {
    position: absolute;
    left: 30px;
    top: 60px;
    width: 255px;
    height: 190px;
    border-radius: 6px;
    background: linear-gradient(135deg, #2f9fb0 0%, #2f9fb0 45%, #b9b3a4 60%, #8e8a82 100%);
  }
  .company-name {
    position: absolute;
    left: 300px;
    top: 118px;
    font-size: 56px;
    font-weight: 700;
    color: var(--brand-blue);
    letter-spacing: 0.5px;
    white-space: nowrap;
  }
  .header-rule {
    position: absolute;
    left: 0; top: 262px;
    width: 100%;
    height: 6px;
    background: linear-gradient(180deg, #c4c8cb, var(--rule-silver));
  }
  .header-band {
    position: absolute;
    left: 0; top: 268px;
    width: 100%;
    height: 18px;
    background: linear-gradient(180deg, var(--brand-blue), var(--brand-blue-deep));
  }
  .card-body {
    position: absolute;
    left: 0; top: 286px;
    width: 100%;
    height: 234px;
    background: linear-gradient(180deg, var(--panel-charcoal) 0%, var(--panel-black) 100%);
    text-align: center;
  }
  .contact-name {
    margin-top: 22px;
    font-size: 40px;
    font-weight: 700;
    color: var(--brand-blue);
    line-height: 1.1;
  }
  .contact-role {
    margin-top: 4px;
    font-size: 24px;
    font-weight: 700;
    color: var(--text-grey);
  }
  .contact-phone {
    margin-top: 30px;
    font-size: 36px;
    font-weight: 700;
    color: var(--text-white);
    letter-spacing: 1px;
  }
  .contact-email {
    margin-top: 4px;
    font-size: 28px;
    font-weight: 500;
    color: var(--text-grey);
  }
</style>
</head>
<body>
  <div class="business-card">
    <header class="card-header">
      <div class="truck-artwork" role="img" aria-label="Illustration of a hook-lift garbage truck tipping a teal waste bin"></div>
      <div class="company-name">Harbor Refuse 342</div>
    </header>
    <div class="header-rule"></div>
    <div class="header-band"></div>
    <section class="card-body">
      <div class="contact-name">Dale Pickett</div>
      <div class="contact-role">Manager</div>
      <div class="contact-phone">0439516204</div>
      <div class="contact-email">harborrefuse342@quillmail.com.au</div>
    </section>
  </div>
</body>
</html>
```